【 概要 】 ご覧いただきありがとうございます。 ウィスキー関連のサイトを運営しているMIRANDE KOVEです。 https://mirande-kove.com/ まずは、4ページをコンペさせていただき、良さそうな方に、24ページお願いしたいと思っております。 熟成樽を購入してくれた方だけでなく、これから熟成樽に興味をもってくださる方にもお渡しする予定です。 手にとった時、すごいブランドだな。ワクワクする商品だな。って思ってもらいたいと思っております。 イメージは、AIで作ってみましたが、さらに良い文章やイメージにしていただけたらなお嬉しいです。 【 コンペ依頼内容 】 ・サイズ:A5 ・ページ数:4ページ ・素材の用意(画像・文章等):画像はAIで作成しました。AI使ってもらっても大丈夫ですが、お願いしたいです。 フリー素材や有料素材でも嬉しいです。 文章はこちらで用意しました。 ぜひ下記のURLからお願いします。 https://slides.pelvora-docs.net/deck/d/7Rm2bXqLw8ZcVtN4yPkJhD0sAeUfG3oQiB5nCxE/view?page=id.p9b71dabdaab_0_14#page=id.p9b71dabdaab_0_14 添付URLの中の説明: 1ページ:デザインイメージ(文字化けあり。2ページ目、3ページ目を参照) 2ページ:1ページの中にある文章 3ページ:1ページの中にある文章 4ページ:デザインイメージ(文字化けあり。5ページ目、6ページ目を参照) 5ページ:4ページの中にある文章 6ページ:4ページの中にある文章 【 デザインイメージ 】 ・ターゲット層:30〜50代の大人の余裕のある男性 ・雰囲気:高級感があり冒険感もある雰囲気(大人の自由研究) ・商品単価:2万円〜3万円前後 その他ご質問等ありましたら、気軽にお問い合わせください。 ご応募をお待ちしております! よろしくお願いします。 |
どの案もすてきでしたが、こちらがイメージにあったため、こちらにさせていただきました。
たくさんの素敵なイラストありがとうございます。

```html
<!DOCTYPE html>
<html lang="ja">
<head>
<meta charset="utf-8">
<title>樽の誕生 — The Birth of a Barrel</title>
<link rel="stylesheet" href="https://fonts.googleapis.com/css2?family=Shippori+Mincho:wght@400;600;700;800&family=Cormorant+Garamond:wght@400;500&family=Pinyon+Script&display=swap">
<style>
  :root{
    --ink:#050505;
    --paper:#f4efe6;
    --muted:#d8d0c2;
    --gold:#b8945a;
    --forest-light:#e9d78a;
    --forest-mid:#5f7d32;
    --forest-dark:#1f3314;
    --fire-hot:#f2a13a;
    --fire-deep:#6a2a0c;
    --shop-warm:#8a6a48;
    --shop-dark:#2b2119;
  }
  *{margin:0;padding:0;box-sizing:border-box}
  html,body{width:1200px;height:850px;overflow:hidden;background:var(--ink)}
  .spread{position:relative;width:1200px;height:850px;background:var(--ink);color:var(--paper);
    font-family:"Shippori Mincho",serif;}
  .frame{position:absolute;inset:8px;border:1px solid var(--gold);pointer-events:none}

  .photo{position:absolute}
  .photo-forest{left:28px;top:28px;width:572px;height:382px;
    background:radial-gradient(ellipse at 55% 25%,var(--forest-light) 0%,#a9b456 18%,var(--forest-mid) 45%,var(--forest-dark) 100%)}
  .photo-fire{left:600px;top:28px;width:572px;height:420px;
    background:
      radial-gradient(circle at 86% 22%,var(--fire-hot) 0%,rgba(106,42,12,.7) 14%,transparent 30%),
      radial-gradient(circle at 70% 42%,#e58a2a 0%,rgba(106,42,12,.6) 10%,transparent 22%),
      radial-gradient(circle at 90% 72%,#f0a040 0%,rgba(106,42,12,.6) 10%,transparent 22%),
      linear-gradient(90deg,#0b0908 0%,#1d1612 45%,#3a2a1f 100%);
    -webkit-mask-image:linear-gradient(180deg,#000 70%,transparent 100%);
            mask-image:linear-gradient(180deg,#000 70%,transparent 100%)}
  .photo-workshop{left:124px;top:592px;width:392px;height:210px;
    background:radial-gradient(ellipse at 60% 40%,var(--shop-warm) 0%,#5a4330 45%,var(--shop-dark) 100%)}

  .title{position:absolute;left:0;width:628px;top:166px;text-align:center;
    font-size:54px;font-weight:800;letter-spacing:4px;line-height:1.2;text-shadow:0 2px 8px rgba(0,0,0,.6)}
  .title-en{position:absolute;left:0;width:628px;top:232px;text-align:center;
    font-family:"Pinyon Script",cursive;font-size:24px;color:var(--paper)}
  .intro{position:absolute;left:108px;top:272px;width:434px;height:88px;background:rgba(10,10,10,.82);
    padding:10px 14px;font-size:13px;line-height:1.55;font-weight:600;text-align:center;letter-spacing:.5px}

  .section-head{position:absolute;left:0;width:628px;top:440px;text-align:center;font-size:25px;font-weight:700;letter-spacing:2px;line-height:1.2}
  .section-body{position:absolute;left:124px;top:490px;width:430px;font-size:12px;line-height:1.8;color:var(--muted)}

  .story{position:absolute;left:620px;top:284px;width:560px}
  .story h2{font-size:26px;font-weight:700;letter-spacing:2px;line-height:32px;margin-bottom:4px;white-space:nowrap}
  .story p{font-size:11px;line-height:16px;color:var(--muted);padding-left:20px;margin-bottom:8px;white-space:nowrap}

  .closing{position:absolute;left:612px;top:680px;width:560px;text-align:center;
    font-family:"Cormorant Garamond",serif;font-size:56px;line-height:1;font-weight:500;letter-spacing:.5px;white-space:nowrap}
  .closing-sub{position:absolute;right:62px;top:748px;font-size:14px;letter-spacing:1px;line-height:1.2}
</style>
</head>
<body>
<main class="spread">
  <div class="photo photo-forest" role="img" aria-label="陽光が差し込む緑の森に立つオークの大木"></div>
  <div class="photo photo-fire" role="img" aria-label="工房で炎に焼かれる樽と燃え上がる火"></div>

  <h1 class="title">樽の誕生</h1>
  <p class="title-en">The Birth of a Barrel</p>
  <p class="intro">ウイスキーの魂は、樽から生まれる。<br>その始まりは、広大な森で年月を重ねた一本のオークから。<br>陽を浴び、風に晒され、やがて職人の手で<br>「命の器」へと形を変えていく。</p>

  <h2 class="section-head">森から工房へ</h2>
  <p class="section-body">乾いた木板が並ぶその場所には、木の香りと熱が満ちている。<br>オークは選別され、鉋削られ、曲げられ、焦がされ、打たれる。<br>一枚一枚板が、円を描くように組み立てられるその瞬間、<br>"ただの木材"から、"熟成の器"へと変わる。</p>
  <div class="photo photo-workshop" role="img" aria-label="樽が並ぶ工房で作業する樽職人"></div>

  <section class="story">
    <h2>炎と煙が生む、生命の香り</h2>
    <p>樽の内側が炎に包まれる。<br>火は敵ではない。<br>それは木の奥に眠る甘みを呼び覚まし、柔らかなカラメル香をもたらす。<br>黒く焦られた木目が、黄金の熟成へと導く。</p>
    <h2>鍛え、封じ、命を吹き込む</h2>
    <p>樽には鉄の留め具が叩き込まれる。<br>密閉を確かめるための水と空気が送り込まれる。<br>一滴の漏れもないと確認されたその瞬間、<br>樽は「熟成の舞台」として完成する。</p>
    <h2>時の息吹を宿して</h2>
    <p>完成した樽は、静かな熟成庫の中で、<br>時をかけて呼吸を繰り返しながら、木と酒がゆるやかに調和し、香りを深めてゆく。<br>そのすべては、木と炎、そして職人の技が生み出す奇跡。</p>
    <h2>— 樽は、語る。</h2>
    <p>木の香りが語り、炎がその力を引き出し、そして時間が、味わいに変わる。<br>一本のオークが、幾千の物語を紡ぐ。</p>
  </section>

  <p class="closing">The Birth of a Barrel</p>
  <p class="closing-sub">— 味わいは、火と木が奏でる詩。</p>

  <div class="frame"></div>
</main>
</body>
</html>
```